Our company, Brisk Ladle Pantry prepares handmade, wholesome meals fully cooked and ready to he...

We are rolling out a line of Artisan Small Batch Salad dressings. Our initial offering is an herb/Dijon based vinaigrette that has pleased our friends and families for years. We would like to see designs that incorporate the colors in our logo ( Green is 107 165 57, Gray is 72 72 74 ) The final design should communicate freshness, herbs ( parsley, onion, lettuce, cherry tomatoes, olives) that are caricatures or line drawings at the top or left side of the label. Some or all of these veggies can be used depending upon space,layout etc. Space should not be crowded. Note: We anticipate having additional offerings in the future under the "brisk toppings" name such as sauces and marinades. The attached drawing is only a concept drawing and we defer to the designer for layout and creativity. Our company name is Brisk Ladle Pantry and we would like to incorporate a "fork" in this label design

Font styles to use
Decorative
Script

Colors

Designer to choose colors to be used in the design.

Requirements
Must have
• Vegetables should be in a caricature or line drawing format.
Nice to have
• I uploaded an MS word document that contains a head shot photo of the owner. We would like to have a whimsical rendition done that we will add to our left or right panel on the label.

```html
<!DOCTYPE html>
<html lang="en">
<head>
<meta charset="utf-8">
<title>Brisk Ladle Pantry – Artisan Vinaigrette Label</title>
<link href="https://fonts.googleapis.com/css2?family=Bebas+Neue&family=Cookie&family=Montserrat:wght@700&family=Roboto:wght@400&display=swap" rel="stylesheet">
<style>
  :root {
    --green: rgb(107,165,57);
    --gray: rgb(72,72,74);
    --paper: #ffffff;
    --leaf-light: #c9df9f;
    --leaf-dark: #5f9a3a;
  }
  html, body {
    margin: 0;
    padding: 0;
    overflow: hidden;
    background: var(--paper);
  }
  .label {
    position: relative;
    width: 1200px;
    height: 598px;
    background: var(--paper);
    overflow: hidden;
  }
  .top-band {
    position: absolute;
    left: 0; top: 0;
    width: 1200px; height: 12px;
    background: var(--gray);
  }
  .brand {
    position: absolute;
    left: 452px; top: 30px;
    width: 316px;
    text-align: center;
  }
  .brand-dot {
    display: block;
    width: 84px; height: 84px;
    margin: 0 auto 10px;
    border-radius: 50%;
    background: var(--green);
  }
  .brand-name {
    margin: 0;
    font-family: 'Montserrat', sans-serif;
    font-weight: 700;
    color: var(--gray);
    line-height: 1;
  }
  .brand-name .main {
    display: block;
    font-size: 43px;
    letter-spacing: -1px;
  }
  .brand-name .sub {
    display: block;
    margin-top: 8px;
    font-size: 20px;
    letter-spacing: 9px;
  }
  .salad-art {
    position: absolute;
    left: 330px; top: 216px;
    width: 232px; height: 194px;
    border-radius: 50% 50% 46% 46% / 52% 52% 48% 48%;
    background: radial-gradient(ellipse at 50% 35%, var(--leaf-light) 0%, #a8cc78 45%, #bcbcbc 80%, #e6e6e6 100%);
  }
  .line-name {
    position: absolute;
    left: 330px; top: 358px;
    width: 232px;
    margin: 0;
    text-align: center;
    font-family: 'Bebas Neue', sans-serif;
    font-size: 38px;
    line-height: 1;
    color: var(--gray);
    letter-spacing: 0.5px;
  }
  .product {
    position: absolute;
    left: 566px; top: 276px;
    width: 330px;
    margin: 0;
    text-align: center;
    font-family: 'Bebas Neue', sans-serif;
    font-weight: 400;
    line-height: 1;
  }
  .product .kind {
    display: block;
    font-size: 67px;
    color: var(--gray);
    letter-spacing: 2px;
  }
  .product .flavour {
    display: block;
    margin-top: 6px;
    font-size: 75px;
    color: var(--green);
    letter-spacing: 2px;
  }
  .owner-portrait {
    position: absolute;
    left: 936px; top: 40px;
    width: 228px; height: 306px;
    border-radius: 40% 40% 18% 18% / 30% 30% 12% 12%;
    background: radial-gradient(ellipse at 50% 55%, #3e3e3e 0%, #6a6a6a 45%, #bdbdbd 75%, rgba(255,255,255,0) 100%);
  }
  .owner-brand {
    position: absolute;
    left: 936px; top: 348px;
    width: 228px;
    margin: 0;
    text-align: center;
    font-family: 'Montserrat', sans-serif;
    font-weight: 700;
    font-size: 25px;
    line-height: 1;
    color: var(--gray);
    letter-spacing: -0.5px;
  }
  .use-band {
    position: absolute;
    left: 303px; top: 466px;
    width: 597px; height: 47px;
    background: var(--gray);
    display: flex;
    align-items: center;
    justify-content: center;
  }
  .use-band p {
    margin: 0;
    font-family: 'Cookie', cursive;
    font-size: 34px;
    color: var(--paper);
    letter-spacing: 0.5px;
  }
  .volume-rule {
    position: absolute;
    top: 565px;
    height: 13px;
    background: var(--gray);
  }
  .volume-rule.left { left: 0; width: 560px; border-radius: 0 6px 6px 0; }
  .volume-rule.right { left: 676px; width: 524px; border-radius: 6px 0 0 6px; }
  .volume {
    position: absolute;
    left: 560px; top: 556px;
    width: 116px;
    margin: 0;
    text-align: center;
    font-family: 'Roboto', sans-serif;
    font-size: 27px;
    line-height: 1;
    color: var(--gray);
  }
</style>
</head>
<body>
<main class="label">
  <div class="top-band"></div>

  <header class="brand">
    <span class="brand-dot"></span>
    <h1 class="brand-name"><span class="main">BRISK LADLE</span><span class="sub">PANTRY</span></h1>
  </header>

  <div class="salad-art" role="img" aria-label="Line drawing of a salad bowl overflowing with lettuce, herbs, cucumber slices and mushrooms"></div>
  <p class="line-name">BRISK TOPPINGS</p>

  <h2 class="product"><span class="kind">ARTISAN</span><span class="flavour">VINAIGRETTE</span></h2>

  <div class="owner-portrait" role="img" aria-label="Whimsical sketch-style portrait of the company owner"></div>
  <p class="owner-brand">BRISK LADLE</p>

  <div class="use-band"><p>· Marinade and Dipping Sauce ·</p></div>

  <div class="volume-rule left"></div>
  <p class="volume">237 ml</p>
  <div class="volume-rule right"></div>
</main>
</body>
</html>
```